Letterhead, business card and email signature design

I have a new company and I would like a professional letterhead, business card and email signature designed. Id like the business card to have room for a photo of the bearer. I'd also like the template to be editable so we can adapt for future members of staff etc.

```html
<!DOCTYPE html>
<html lang="en">
<head>
<meta charset="utf-8">
<title>Altair Netlink – Letterhead</title>
<link rel="stylesheet" href="https://fonts.googleapis.com/css2?family=Open+Sans:wght@400;700&display=swap">
<style>
  :root {
    --backdrop: #1c1d1f;
    --paper: #f7f7f7;
    --navy: #0d2f5e;
    --magenta: #b8114f;
    --magenta-soft: #c8336a;
    --watermark-light: #f3f3f3;
    --watermark-dark: #e4e4e4;
  }
  * { box-sizing: border-box; margin: 0; padding: 0; }
  html, body {
    width: 1200px;
    height: 960px;
    overflow: hidden;
    background: var(--backdrop);
    font-family: "Open Sans", Arial, sans-serif;
  }
  .letterhead {
    position: absolute;
    left: 260px;
    top: 40px;
    width: 680px;
    height: 880px;
    background: var(--paper);
    color: var(--navy);
  }
  .brand {
    position: absolute;
    left: 58px;
    top: 66px;
    display: flex;
    align-items: center;
    gap: 14px;
  }
  .brand-dot {
    width: 64px;
    height: 64px;
    border-radius: 50%;
    background: var(--navy);
  }
  .brand-name {
    font-size: 24px;
    font-weight: 700;
    letter-spacing: 0.5px;
    color: var(--navy);
  }
  .watermark {
    position: absolute;
    left: 160px;
    top: 250px;
    width: 370px;
    height: 370px;
    border-radius: 50%;
    background: radial-gradient(circle at 35% 30%, var(--watermark-light), var(--watermark-dark));
  }
  .footer {
    position: absolute;
    left: 20px;
    right: 36px;
    bottom: 28px;
    display: flex;
    align-items: flex-end;
    gap: 20px;
    font-size: 11.5px;
    line-height: 1.35;
  }
  .footer-accent {
    width: 92px;
    height: 118px;
    flex: none;
    background: linear-gradient(160deg, var(--magenta), var(--magenta-soft));
  }
  .address { margin-bottom: 22px; }
  .address b { font-weight: 700; }
  .numbers { margin-left: 32px; margin-top: 4px; }
  .email { margin-left: auto; margin-bottom: 70px; }
  .email b { font-weight: 700; }
</style>
</head>
<body>
  <main class="letterhead">
    <header class="brand">
      <span class="brand-dot"></span>
      <span class="brand-name">ALTAIR NETLINK</span>
    </header>

    <div class="watermark" aria-hidden="true"></div>

    <footer class="footer">
      <div class="footer-accent" role="img" aria-label="Magenta decorative block motif"></div>
      <div class="address">
        <p><b>Address:</b> Altair Netlink&nbsp; 240 Harlow Ave</p>
        <p>Brookfield, GA 30412</p>
        <div class="numbers">
          <p><b>Phone:</b> 555.310.0141</p>
          <p><b>toll-free:</b> 800.555.0192</p>
          <p><b>fax:</b> 555.310.0142</p>
        </div>
      </div>
      <p class="email"><b>Email:</b> info@altairnetlink.com</p>
    </footer>
  </main>
</body>
</html>
```